Web design - holistic filmmaker

I need a design for my new website.

I am a holistic filmmaker, ie I make films for healers, alternative practitioners, spiritual people and institutions that offer training in this field.

The design should be noble, bright, convey the feeling of space and expanse and have some particularly beautiful color accents.

The structure is: start page, offer, references, about me, imprint.

As an idea for the start page, I thought that either I could introduce myself as a filmmaker and my offer, or we could start right on the start page with the references, ie photos and links to already realized projects.

If you want more information or an exchange, I'd love to hear from you. At the moment I just don't know how to describe it better.

The winner will then be asked to design a logo.

Target Market(s)

healers, alternative practitioners, spiritual people and institutions that offer training in this field

Industry/Entity Type

Film production

Number of Pages Required

3 page

```html
<!DOCTYPE html>
<html lang="en">
<head>
<meta charset="utf-8">
<title>Lumen – Holistic Filmmaker</title>
<link href="https://fonts.googleapis.com/css2?family=Poppins:wght@500;600;700&family=Roboto:wght@400;500&display=swap" rel="stylesheet">
<style>
:root{
  --ink:#111111;
  --black:#000000;
  --footer:#0d0d0d;
  --footer-bar:#050505;
  --white:#ffffff;
  --text:#555555;
  --muted:#9a9a9a;
  --sky-top:#cfc9c0;
  --sky-mid:#e9dcc6;
  --sun:#f6e7c8;
  --hill:#3a3632;
  --photo:#6f6560;
}
*{margin:0;padding:0;box-sizing:border-box}
html,body{width:1200px;height:3292px;overflow:hidden;background:var(--white)}
body{font-family:'Roboto',sans-serif;color:var(--text);position:relative}
.heading{font-family:'Poppins',sans-serif;font-weight:700;letter-spacing:2px;text-transform:uppercase}
.btn{display:inline-block;background:var(--ink);color:var(--white);font-family:'Poppins',sans-serif;font-weight:600;font-size:14px;letter-spacing:1px;padding:12px 24px;text-transform:uppercase}

/* hero */
.hero{position:absolute;top:0;left:0;width:1200px;height:660px;overflow:hidden;
  background:linear-gradient(180deg,#8d867e 0%,var(--sky-top) 22%,var(--sky-mid) 48%,var(--sun) 58%,#9a8f84 72%,var(--hill) 100%)}
.hero-header{position:absolute;top:0;left:0;width:100%;height:100px;background:linear-gradient(180deg,rgba(0,0,0,.55),rgba(0,0,0,0))}
.logo{position:absolute;left:112px;top:32px;color:var(--white);font-family:'Poppins',sans-serif;font-weight:600;font-size:28px;letter-spacing:3px}
.nav{position:absolute;left:380px;top:40px;display:flex;gap:30px}
.nav a{color:var(--white);font-family:'Poppins',sans-serif;font-size:15px;font-weight:500;text-decoration:none;letter-spacing:1px;padding-bottom:6px}
.nav a.active{border-bottom:2px solid var(--white)}
.social{position:absolute;left:1050px;top:38px;display:flex;gap:14px}
.social span{width:20px;height:20px;border:2px solid var(--white);border-radius:50%}
.hero-title{position:absolute;top:255px;width:100%;text-align:center;color:var(--ink);font-size:56px}
.hero .btn{position:absolute;top:352px;left:538px;font-size:13px;padding:12px 22px}
.dots{position:absolute;left:1144px;top:216px;display:flex;flex-direction:column;gap:20px}
.dots span{width:14px;height:14px;border-radius:50%;background:var(--white);opacity:.9}
.tab{position:absolute;left:576px;top:640px;width:48px;height:24px}

/* about */
.about-frame{position:absolute;left:92px;top:760px;width:420px;height:430px;border:6px solid var(--ink)}
.about-photo{position:absolute;left:112px;top:780px;width:480px;height:480px;background:linear-gradient(160deg,#8e8880,var(--photo) 50%,#d09a4a)}
.about-title{position:absolute;left:632px;top:776px;font-size:48px;color:var(--ink)}
.about-text{position:absolute;left:632px;top:846px;width:468px;font-size:15.5px;line-height:25px}
.about-text p+p{margin-top:24px}
.about .btn{position:absolute;left:632px;top:1226px}

/* projects */
.projects{position:absolute;top:1372px;left:0;width:1200px;height:888px;background:var(--black)}
.projects-title{position:absolute;top:80px;width:100%;text-align:center;color:var(--white);font-size:50px}
.thumb{position:absolute;width:472px;height:290px;border:3px solid var(--white);display:flex;align-items:center;justify-content:center}
.t1{left:112px;top:162px;background:linear-gradient(135deg,#c89a86,#d7c3b8 50%,#9d7e72)}
.t2{left:618px;top:162px;background:linear-gradient(135deg,#a4a19c,#6f6c69 50%,#d9d6d1)}
.t3{left:112px;top:500px;background:linear-gradient(135deg,#c9d7e6,#b0a79e 50%,#5b4a46)}
.t4{left:618px;top:500px;background:linear-gradient(135deg,#e7e3de,#9a8e86 50%,#3e3a3a)}

/* offer */
.offer-title{position:absolute;top:2362px;width:100%;text-align:center;color:var(--ink);font-size:50px}
.offer-text{position:absolute;left:186px;top:2430px;width:828px;text-align:center;font-size:15px;line-height:24px}
.offer-text p+p{margin-top:24px}
.offer .btn{position:absolute;left:538px;top:2718px}

/* footer */
.footer{position:absolute;top:2960px;left:0;width:1200px;height:240px;background:var(--footer);color:var(--white)}
.fcol{position:absolute;top:44px}
.fcol h3{font-family:'Poppins',sans-serif;font-size:20px;font-weight:600;margin-bottom:18px}
.fcol li{list-style:none;font-size:15px;line-height:29px;padding-left:22px;position:relative}
.fcol li::before{content:"";position:absolute;left:2px;top:11px;border-left:7px solid var(--white);border-top:5px solid transparent;border-bottom:5px solid transparent}
.contact li{padding-left:34px;width:230px}
.contact li::before{display:none}
.contact svg{position:absolute;left:0;top:6px}
.bar{position:absolute;top:3200px;left:0;width:1200px;height:92px;background:var(--footer-bar);color:var(--white);text-align:center;font-size:14px;line-height:92px}
</style>
</head>
<body>

<section class="hero">
  <div role="img" aria-label="Silhouette of a person in a yoga pose on a mountain top at sunrise" style="position:absolute;inset:0"></div>
  <header class="hero-header">
    <div class="logo">LUMEN</div>
    <nav class="nav">
      <a class="active">HOME</a><a>OFFER</a><a>REFERENCES</a><a>ABOUT ME</a><a>IMPRINT</a>
    </nav>
    <div class="social"><span></span><span></span><span></span><span></span></div>
  </header>
  <h1 class="heading hero-title">Holistic Filmmaker</h1>
  <a class="btn">Get Started</a>
  <div class="dots"><span></span><span></span><span></span><span></span></div>
  <svg class="tab" viewBox="0 0 48 24"><path d="M0 24 L24 0 L48 24Z" fill="#fff"/><path d="M18 16 L24 10 L30 16" stroke="#111" stroke-width="2.5" fill="none"/></svg>
</section>

<section class="about">
  <div class="about-frame"></div>
  <div class="about-photo" role="img" aria-label="Portrait of the filmmaker in an orange shirt"></div>
  <h2 class="heading about-title">About Me</h2>
  <div class="about-text">
    <p>My name is Lumen and I make films - with enthusiasm and with all my heart. I am a holistic filmmaker. At the end of the Ninties, I was faced with the question of whether I should work in alternative medicine or in the film industry myself. Professionally, I decided to do film at the time, but that spiritual path and my passion for so-called alternative healing methods have accompanied me almost as intensely ever since.</p>
    <p>My cinematic path took me literally from cable man to cameraman, director and producer. It all started in 1993 as a camera assistant at an international TV news agency. In the years that followed I worked in various positions on numerous national and international television productions, feature films and documentaries, commercials and live productions.</p>
  </div>
  <a class="btn">Learn More</a>
</section>

<section class="projects">
  <h2 class="heading projects-title">Our Projects</h2>
  <div class="thumb t1" role="img" aria-label="Video still: woman speaking in a bright room">
    <svg width="80" height="80" viewBox="0 0 80 80"><circle cx="40" cy="40" r="38" fill="rgba(0,0,0,.55)" stroke="#fff" stroke-width="3"/><path d="M32 25 L58 40 L32 55Z" fill="#fff"/></svg></div>
  <div class="thumb t2" role="img" aria-label="Video still: two people in conversation">
    <svg width="80" height="80" viewBox="0 0 80 80"><circle cx="40" cy="40" r="38" fill="rgba(0,0,0,.55)" stroke="#fff" stroke-width="3"/><path d="M32 25 L58 40 L32 55Z" fill="#fff"/></svg></div>
  <div class="thumb t3" role="img" aria-label="Video still: woman speaking outdoors">
    <svg width="80" height="80" viewBox="0 0 80 80"><circle cx="40" cy="40" r="38" fill="rgba(0,0,0,.55)" stroke="#fff" stroke-width="3"/><path d="M32 25 L58 40 L32 55Z" fill="#fff"/></svg></div>
  <div class="thumb t4" role="img" aria-label="Video still: speaker on a stage">
    <svg width="80" height="80" viewBox="0 0 80 80"><circle cx="40" cy="40" r="38" fill="rgba(0,0,0,.55)" stroke="#fff" stroke-width="3"/><path d="M32 25 L58 40 L32 55Z" fill="#fff"/></svg></div>
</section>

<section class="offer">
  <h2 class="heading offer-title">Our Offer</h2>
  <div class="offer-text">
    <p>Einen Film zu drehen ist immer auch eine Reise zu sich selbst. Mit achtsamen Mitteln und ohne Spezialeffekte begleite ich Sie auf Ihrem Weg. Mit Wissen und Gespür für das Wesentliche erzähle ich von Menschen, Heilweisen und Orten. Filme für Aufgeschlossene richten sich an alle Menschen und Institutionen, deren Denken nach Wahrhaftigkeit im Tun strebt. Sinnvolles Handeln, hochwertige Bildgestaltung und eine informative und verständliche Vermittlung komplexer Sachverhalte sind Leidenschaft und Grundlage meiner Filmarbeit.</p>
    <p>Als Full-Service-Dienstleister biete ich von der Beratung und Konzeption bis zum fertigen Film alles aus einer Hand: Werbefilme, Imagefilme, Unternehmenspräsentationen, Interviews, Dokumentationen, Eventaufzeichnungen, auch mit mehreren Kameras oder Live Streams – unterstützt werde ich dabei von einem langjährigen und bewährten Netzwerk an freien Mitarbeitern, Kreativen und technischen Dienstleistern.</p>
  </div>
  <a class="btn">Learn More</a>
</section>

<footer class="footer">
  <div class="fcol" style="left:212px">
    <h3>Quick Links</h3>
    <ul><li>Home</li><li>About Me</li><li>Offer</li><li>References</li><li>Imprint</li></ul>
  </div>
  <div class="fcol" style="left:472px">
    <h3>Support</h3>
    <ul><li>Support</li><li>Faq</li><li>Contact</li><li>Privacy policy</li><li>Terms of condition</li></ul>
  </div>
  <div class="fcol contact" style="left:760px">
    <h3>Contact Us</h3>
    <ul>
      <li><svg width="16" height="20" viewBox="0 0 16 20"><path d="M8 0C3.6 0 0 3.4 0 7.6 0 13 8 20 8 20s8-7 8-12.4C16 3.4 12.4 0 8 0z" fill="#fff"/><circle cx="8" cy="7.5" r="3" fill="#0d0d0d"/></svg>123,Lorem ipsum dolor amet, consectetur</li>
      <li style="margin-top:14px"><svg width="18" height="18" viewBox="0 0 24 24"><path d="M6.6 10.8c1.4 2.8 3.8 5.1 6.6 6.6l2.2-2.2c.3-.3.7-.4 1-.2 1.1.4 2.3.6 3.6.6.6 0 1 .4 1 1V20c0 .6-.4 1-1 1C10.6 21 3 13.4 3 4c0-.6.4-1 1-1h3.5c.6 0 1 .4 1 1 0 1.3.2 2.5.6 3.6.1.3 0 .7-.2 1z" fill="#fff"/></svg>+1 888 888 8888</li>
      <li><svg width="18" height="16" viewBox="0 0 24 18"><rect x="1" y="1" width="22" height="16" rx="2" fill="#fff"/><path d="M2 2l10 8 10-8" stroke="#0d0d0d" stroke-width="2" fill="none"/></svg>info@lumenfilm.example</li>
    </ul>
  </div>
</footer>
<div class="bar">© Copyrights 2023 | All rights reserved</div>

</body>
</html>
```